Mobile Interface Design

Take an existing website design and create a Mobile interface that is creative and easy to navigate. Background programming and stuff already accomplished... need a Graphic Designer with Mobile UI expertise. Need it done quickly in 1-2 weeks.
Go to http://demo.fairwaypulse-example.com. Signup using invitation code "milvantour" - we need the pick players screen designed for a mobile platform. We have some ideas regarding the layout of the screen. I will upload a mockup. We need to stick to current design site as much as possible but also provide a better mobile site experience.
Notes of the attached file:
The header will have Teebeacon logo, Messages icon, Points and menu (lines).
Ignore second bar
Tournament Info will be a scroll down box (mobile expand layer)
Tokens bar will have the tokens from the web page 100/40
The field - will be the players from the website - will show rank, photo, name, token value (20) and a check box - to select. the check box will change the color of the layer. At the top - the filters will be similar to filters on website. There will be a clear/show selected button to filter list (not required to show on design) - at bottom "Next Choose Winner" button.
We need footer with menu links "Pick Players", "My Compass", My Games", "My Profile".
If you have any specific questions, please let me know before starting on it.
Updates
This is not a contest for everyone looking to work on it. If you submit your portfolio and ideas, we will work with them directly on the design/delivery. This is my first time posting a project and didn't realize I created a contest.
Target Market(s)
iOS and Android
Look and feel
Each slider illustrates characteristics of the customer's brand and the style your logo design should communicate.

```html
<!DOCTYPE html>
<html lang="en">
<head>
<meta charset="utf-8">
<title>Teebeacon – Pick Players</title>
<link rel="stylesheet" href="https://fonts.googleapis.com/css2?family=Arimo:wght@400;700&display=swap">
<style>
:root{
  --navy:#1f3b63;
  --navy-dark:#162c4c;
  --navy-btn:#24426e;
  --ink:#121a26;
  --light:#f4f4f4;
  --light-2:#dcdcdc;
  --line:#cfd3d8;
  --green:#5a8f3a;
  --green-dark:#467529;
  --logo:#4f7d32;
  --red:#d9261c;
  --white:#ffffff;
  --black:#0c0c0c;
}
*{box-sizing:border-box;margin:0;padding:0}
html,body{width:1200px;height:2557px;overflow:hidden;background:var(--white)}
body{font-family:"Arimo",Arial,sans-serif;color:var(--ink)}
.app{width:1200px;height:2557px;display:flex;flex-direction:column}

.header{height:190px;background:linear-gradient(#ffffff,#e6e6e6);display:flex;align-items:center;padding:0 44px 0 50px;border-bottom:2px solid #c9c9c9}
.brand{font-size:84px;font-weight:400;color:var(--logo);letter-spacing:-2px;flex:1}
.hbtn{height:72px;border-radius:10px;background:linear-gradient(#2c4f82,var(--navy-dark));border:2px solid #0f213b;color:var(--white);font-weight:700;font-size:24px;display:flex;align-items:center;justify-content:center;gap:14px;position:relative;margin-left:42px}
.mail{width:158px}
.points{width:161px}
.menu{width:113px}
.badge{position:absolute;top:-22px;right:-4px;width:40px;height:40px;border-radius:50%;background:var(--red);color:var(--white);font-size:22px;display:flex;align-items:center;justify-content:center;border:2px solid #fff}

.tinfo{height:95px;background:var(--navy);display:flex;align-items:center;justify-content:space-between;padding:0 40px 0 57px;color:var(--white);font-size:26px;font-weight:400}
.tokens{height:95px;background:linear-gradient(#fafafa,var(--light-2));display:flex;align-items:center;gap:43px;padding-left:125px}
.token{height:60px;border-radius:8px;background:linear-gradient(#3a3a3a,var(--black));color:var(--white);font-weight:700;font-size:25px;display:flex;align-items:center;justify-content:center}

.filters{height:100px;background:linear-gradient(#2a4a78,var(--navy-dark));display:flex;align-items:center;justify-content:space-between;padding:0 38px 0 27px}
.pill-light{height:57px;border-radius:8px;background:linear-gradient(#ffffff,#dcdcdc);border:1px solid #9aa4b0;font-size:27px;font-weight:700;color:#1d2a3c;display:flex;align-items:center}
.field{width:186px;justify-content:center}
.sort{width:294px;padding-left:24px;justify-content:space-between}
.sort .caret{width:66px;height:100%;border-left:2px solid #9aa4b0;display:flex;align-items:center;justify-content:center}

.players{list-style:none;flex:none}
.player{height:177px;display:flex;align-items:center;background:linear-gradient(#ffffff,#ececec);border-bottom:3px solid var(--line)}
.photo{width:109px;height:114px;margin-left:57px;background:linear-gradient(160deg,#8aa76a,#d3803a 70%,#7a5a3c);flex:none}
.who{margin-left:67px;width:252px;flex:none;overflow:hidden}
.name{font-size:28px;font-weight:700;white-space:nowrap;overflow:hidden;text-overflow:ellipsis}
.rank{font-size:17px;font-weight:700;margin-top:10px;white-space:nowrap}
.flag{margin-left:10px;width:50px;height:34px;flex:none}
.stats{margin-left:83px;width:252px;height:60px;flex:none;position:relative;background:linear-gradient(#2d4f80,var(--navy-dark));color:var(--white);font-size:24px;border-radius:10px;display:flex;align-items:center;padding-left:28px;white-space:nowrap}
.stats::before{content:"";position:absolute;left:-16px;top:50%;margin-top:-14px;border-style:solid;border-width:14px 16px 14px 0;border-color:transparent #24426e transparent transparent}
.go{margin-left:auto;margin-right:44px;width:102px;height:90px;flex:none;border-radius:8px;background:linear-gradient(#3b3b3b 0 50%,var(--black) 50%);display:flex;align-items:center;justify-content:center}

.actions{height:126px;background:var(--white);display:flex;align-items:center;justify-content:space-between;padding:0 33px 0 52px}
.btn{height:69px;border-radius:9px;color:var(--white);font-weight:700;font-size:25px;display:flex;align-items:center;justify-content:center;white-space:nowrap}
.clear{width:177px;background:linear-gradient(#2d4f80,var(--navy-dark))}
.next{width:333px;background:linear-gradient(#6ea64a,var(--green-dark))}

.footer{height:181px;background:linear-gradient(var(--navy-btn),#9aa8bf);display:flex;align-items:center;padding:0 30px 0 27px}
.nav{display:flex;gap:30px;flex:1}
.nav a{height:62px;padding:0 18px;border-radius:9px;background:linear-gradient(#ffffff,#d6d6d6);color:#1d2a3c;font-size:24px;font-weight:700;text-decoration:none;display:flex;align-items:center;white-space:nowrap}
.social{display:flex;gap:12px}
.social span{width:50px;height:50px;border-radius:6px;background:#dfe4ec;border:2px solid #7d8aa0}
</style>
</head>
<body>
<div class="app">
  <header class="header">
    <div class="brand">Teebeacon</div>
    <div class="hbtn mail">
      <svg width="40" height="28" viewBox="0 0 40 28"><rect x="1" y="1" width="38" height="26" rx="2" fill="#fff"/><path d="M2 2 20 16 38 2" fill="none" stroke="#8aa0bf" stroke-width="2.5"/></svg>
      Mail<span class="badge">0</span>
    </div>
    <div class="hbtn points">3420 Pts</div>
    <div class="hbtn menu" aria-label="Menu">
      <svg width="50" height="38" viewBox="0 0 50 38"><rect y="2" width="50" height="6" rx="2" fill="#fff"/><rect y="16" width="50" height="6" rx="2" fill="#fff"/><rect y="30" width="50" height="6" rx="2" fill="#fff"/></svg>
    </div>
  </header>

  <section class="tinfo">
    <span>TOURNAMENT INFO</span>
    <svg width="46" height="46" viewBox="0 0 46 46"><circle cx="23" cy="23" r="22" fill="#dfe6f0"/><path d="M13 18 23 28 33 18" fill="none" stroke="#1f3b63" stroke-width="5" stroke-linecap="round"/></svg>
  </section>

  <section class="tokens">
    <div class="token" style="width:174px">TOKENS</div>
    <div class="token" style="width:337px">100 PLAYERS TOKEN</div>
    <div class="token" style="width:340px">100 BACK UP&nbsp; TOKEN</div>
  </section>

  <section class="filters">
    <div class="pill-light field">Field</div>
    <div class="pill-light sort">Sort by Date
      <span class="caret"><svg width="26" height="16" viewBox="0 0 26 16"><path d="M3 3 13 13 23 3" fill="none" stroke="#1f3b63" stroke-width="4"/></svg></span>
    </div>
  </section>

  <ul class="players">
    <li class="player"><div class="photo" role="img" aria-label="Golfer portrait"></div><div class="who"><div class="name">Rowan Galloway</div><div class="rank">WORLD RANKING: 42</div></div><svg class="flag" viewBox="0 0 50 34"><rect width="50" height="34" fill="#fff"/><g fill="#c8232c"><rect y="0" width="50" height="4"/><rect y="8" width="50" height="4"/><rect y="16" width="50" height="4"/><rect y="24" width="50" height="4"/><rect y="31" width="50" height="3"/></g><rect width="22" height="18" fill="#2a3f7a"/></svg><div class="stats">Player Statistics</div><div class="go"><svg width="30" height="40" viewBox="0 0 30 40"><path d="M8 6 22 20 8 34" fill="none" stroke="#fff" stroke-width="3"/></svg></div></li>
    <li class="player"><div class="photo" role="img" aria-label="Golfer mid-swing" style="background:linear-gradient(160deg,#9cb574,#e8e8e8 60%,#7d9660)"></div><div class="who"><div class="name">Jonas Brekke</div><div class="rank">WORLD RANKING: 42</div></div><svg class="flag" viewBox="0 0 50 34"><rect width="50" height="34" fill="#263f85"/><path d="M0 0 50 34M50 0 0 34" stroke="#fff" stroke-width="7"/><path d="M0 0 50 34M50 0 0 34" stroke="#c8232c" stroke-width="2.5"/><rect x="19" width="12" height="34" fill="#fff"/><rect y="11" width="50" height="12" fill="#fff"/><rect x="22" width="6" height="34" fill="#c8232c"/><rect y="14" width="50" height="6" fill="#c8232c"/></svg><div class="stats">Player Statistics</div><div class="go"><svg width="30" height="40" viewBox="0 0 30 40"><path d="M8 6 22 20 8 34" fill="none" stroke="#fff" stroke-width="3"/></svg></div></li>
    <li class="player"><div class="photo" role="img" aria-label="Golfer follow-through" style="background:linear-gradient(160deg,#6f7a62,#3d4a38 60%,#9a9a8a)"></div><div class="who"><div class="name">Ben Carver</div><div class="rank">WORLD RANKING: 42</div></div><svg class="flag" viewBox="0 0 50 34"><rect width="50" height="34" fill="#fff"/><g fill="#c8232c"><rect y="0" width="50" height="4"/><rect y="8" width="50" height="4"/><rect y="16" width="50" height="4"/><rect y="24" width="50" height="4"/><rect y="31" width="50" height="3"/></g><rect width="22" height="18" fill="#2a3f7a"/></svg><div class="stats">Player Statistics</div><div class="go"><svg width="30" height="40" viewBox="0 0 30 40"><path d="M8 6 22 20 8 34" fill="none" stroke="#fff" stroke-width="3"/></svg></div></li>
    <li class="player"><div class="photo" role="img" aria-label="Golfer in white on the course" style="background:linear-gradient(160deg,#3f6a34,#e6e6e6 65%,#56803f)"></div><div class="who"><div class="name">Mark Whitley</div><div class="rank">WORLD RANKING: 42</div></div><svg class="flag" viewBox="0 0 50 34"><rect width="50" height="34" fill="#fff"/><g fill="#c8232c"><rect y="0" width="50" height="4"/><rect y="8" width="50" height="4"/><rect y="16" width="50" height="4"/><rect y="24" width="50" height="4"/><rect y="31" width="50" height="3"/></g><rect width="22" height="18" fill="#2a3f7a"/></svg><div class="stats">Player Statistics</div><div class="go"><svg width="30" height="40" viewBox="0 0 30 40"><path d="M8 6 22 20 8 34" fill="none" stroke="#fff" stroke-width="3"/></svg></div></li>
    <li class="player"><div class="photo" role="img" aria-label="Golfer close-up in cap" style="background:linear-gradient(160deg,#2a2a2a,#e3b49a 45%,#f2f2f2)"></div><div class="who"><div class="name">Rowan Galloway</div><div class="rank">WORLD RANKING: 42</div></div><svg class="flag" viewBox="0 0 50 34"><rect width="50" height="34" fill="#fff"/><g fill="#c8232c"><rect y="0" width="50" height="4"/><rect y="8" width="50" height="4"/><rect y="16" width="50" height="4"/><rect y="24" width="50" height="4"/><rect y="31" width="50" height="3"/></g><rect width="22" height="18" fill="#2a3f7a"/></svg><div class="stats">Player Statistics</div><div class="go"><svg width="30" height="40" viewBox="0 0 30 40"><path d="M8 6 22 20 8 34" fill="none" stroke="#fff" stroke-width="3"/></svg></div></li>
    <li class="player"><div class="photo" role="img" aria-label="Golfer in orange shirt" style="background:linear-gradient(160deg,#1f2b1c,#c8612a 65%,#e07a32)"></div><div class="who"><div class="name">Jonas Brekke</div><div class="rank">WORLD RANKING: 42</div></div><svg class="flag" viewBox="0 0 50 34"><rect width="50" height="34" fill="#263f85"/><path d="M0 0 50 34M50 0 0 34" stroke="#fff" stroke-width="7"/><path d="M0 0 50 34M50 0 0 34" stroke="#c8232c" stroke-width="2.5"/><rect x="19" width="12" height="34" fill="#fff"/><rect y="11" width="50" height="12" fill="#fff"/><rect x="22" width="6" height="34" fill="#c8232c"/><rect y="14" width="50" height="6" fill="#c8232c"/></svg><div class="stats">Player Statistics</div><div class="go"><svg width="30" height="40" viewBox="0 0 30 40"><path d="M8 6 22 20 8 34" fill="none" stroke="#fff" stroke-width="3"/></svg></div></li>
    <li class="player"><div class="photo" role="img" aria-label="Golfer celebrating" style="background:linear-gradient(160deg,#8aa76a,#d3803a 70%,#7a5a3c)"></div><div class="who"><div class="name">Ben Carver</div><div class="rank">WORLD RANKING: 42</div></div><svg class="flag" viewBox="0 0 50 34"><rect width="50" height="34" fill="#fff"/><g fill="#c8232c"><rect y="0" width="50" height="4"/><rect y="8" width="50" height="4"/><rect y="16" width="50" height="4"/><rect y="24" width="50" height="4"/><rect y="31" width="50" height="3"/></g><rect width="22" height="18" fill="#2a3f7a"/></svg><div class="stats">Player Statistics</div><div class="go"><svg width="30" height="40" viewBox="0 0 30 40"><path d="M8 6 22 20 8 34" fill="none" stroke="#fff" stroke-width="3"/></svg></div></li>
    <li class="player"><div class="photo" role="img" aria-label="Golfer walking the course" style="background:linear-gradient(160deg,#2f4a2a,#d26a2e 60%,#3a5a30)"></div><div class="who"><div class="name">Mark Whitley</div><div class="rank">WORLD RANKING: 42</div></div><svg class="flag" viewBox="0 0 50 34"><rect width="50" height="34" fill="#fff"/><g fill="#c8232c"><rect y="0" width="50" height="4"/><rect y="8" width="50" height="4"/><rect y="16" width="50" height="4"/><rect y="24" width="50" height="4"/><rect y="31" width="50" height="3"/></g><rect width="22" height="18" fill="#2a3f7a"/></svg><div class="stats">Player Statistics</div><div class="go"><svg width="30" height="40" viewBox="0 0 30 40"><path d="M8 6 22 20 8 34" fill="none" stroke="#fff" stroke-width="3"/></svg></div></li>
    <li class="player"><div class="photo" role="img" aria-label="Golfer driving off the tee" style="background:linear-gradient(160deg,#a9c2de,#d9813f 55%,#6f8c55)"></div><div class="who"><div class="name">Mark Whitley</div><div class="rank">WORLD RANKING: 42</div></div><svg class="flag" viewBox="0 0 50 34"><rect width="50" height="34" fill="#fff"/><g fill="#c8232c"><rect y="0" width="50" height="4"/><rect y="8" width="50" height="4"/><rect y="16" width="50" height="4"/><rect y="24" width="50" height="4"/><rect y="31" width="50" height="3"/></g><rect width="22" height="18" fill="#2a3f7a"/></svg><div class="stats">Player Statistics</div><div class="go"><svg width="30" height="40" viewBox="0 0 30 40"><path d="M8 6 22 20 8 34" fill="none" stroke="#fff" stroke-width="3"/></svg></div></li>
    <li class="player"><div class="photo" role="img" aria-label="Golfer in blue on the green" style="background:linear-gradient(160deg,#b9c27a,#3a5fb0 60%,#8aa060)"></div><div class="who"><div class="name">Mark Whitley</div><div class="rank">WORLD RANKING: 42</div></div><svg class="flag" viewBox="0 0 50 34"><rect width="50" height="34" fill="#fff"/><g fill="#c8232c"><rect y="0" width="50" height="4"/><rect y="8" width="50" height="4"/><rect y="16" width="50" height="4"/><rect y="24" width="50" height="4"/><rect y="31" width="50" height="3"/></g><rect width="22" height="18" fill="#2a3f7a"/></svg><div class="stats">Player Statistics</div><div class="go"><svg width="30" height="40" viewBox="0 0 30 40"><path d="M8 6 22 20 8 34" fill="none" stroke="#fff" stroke-width="3"/></svg></div></li>
  </ul>

  <section class="actions">
    <div class="btn clear">CLEAR</div>
    <div class="btn next">NEXT CHOOSE WINNER</div>
  </section>

  <footer class="footer">
    <nav class="nav">
      <a href="#">Pick Player</a>
      <a href="#">MY COMPASS</a>
      <a href="#">MY GAMES</a>
      <a href="#">MY PROFILE</a>
    </nav>
    <div class="social" aria-label="Social links"><span></span><span></span><span></span></div>
  </footer>
</div>
</body>
</html>
```